Update/re-design of a brochure for a summer camp for abused children

We are looking for an update to our tri-fold 8.5' x 11" brochure for Bright Harbor YOUTH Camp of Ventura. Our camp is one of a network of 188 church-sponsored camps in the U.S. and 23 camps in four foreign countries. We take abused, abandoned and neglected children (ages 7-11) to camp for "a week of positive memories." Our brochure is used primarily to recruit volunteers and donors/supporters. Our current brochure and logo is attached; text will only have some minor edits from the attached. Red in the logo must use Pantone 186; purple in the logo must use Pantone 267. Photos should depict children ages 7-11 only. Photos can show boys and girls playing, swimming, hiking, horseback riding, in a petting zoo, doing arts & crafts, around a camp fire, at a birthday party, riding bikes, playing games, etc. Pictures could include any of the attached photos, but other images may be used too. www.ventura.brightharboryouth-example.org

Target Market(s)

Our brochure is used primarily to recruit volunteers and donors/supporters at church and away in the community..

Industry/Entity Type

Church

Font styles to use
Other font styles liked:
• Myriad Pro, Arial Narrow or Trade Gothic LT STD

Requirements
Must have
• Bright Harbor YOUTH logo. Tear-off interest card, but the back side of the tear-off should be info that is not critical to the reader later like the current design has BHY's background/history on the backside of the tear-off.
Nice to have
• Should have photos of kids, ages 7-11, interacting in positive, fun activities with one another and/or with adults. Genders could be mixed, but for the most part, only male volunteers are with boys, and only female volunteers are with girls.
Should not have
• Negative images. Kids younger than 7 or older than 11.

```html
<!DOCTYPE html>
<html lang="en">
<head>
<meta charset="utf-8">
<title>Bright Harbor YOUTH Camp – Tri-fold Brochure</title>
<link href="https://fonts.googleapis.com/css2?family=Arimo:ital,wght@0,400;0,700;1,400&display=swap" rel="stylesheet">
<style>
:root{
  --red:#c8102e;
  --purple:#5f259f;
  --ink:#2b2b2b;
  --paper:#ffffff;
  --bg:#e6e6e6;
  --rule:#b9b9c6;
  --grass:#6f9a4a;
}
*{box-sizing:border-box;margin:0;padding:0}
html,body{width:761px;height:1200px;overflow:hidden;background:var(--bg)}
body{font-family:"Arimo",Arial,sans-serif;color:var(--ink);position:relative}
.sheet{position:absolute;left:0;width:761px;height:585px;background:var(--paper);display:grid;grid-template-columns:repeat(3,1fr);box-shadow:0 2px 6px rgba(0,0,0,.25)}
.sheet--outside{top:6px}
.sheet--inside{top:607px}
.panel{position:relative;overflow:hidden;padding:36px 16px 14px;border-right:1px solid #ececf0;font-size:7.2px;line-height:1.38}
.panel:last-child{border-right:none}
.top-band{position:absolute;top:0;left:0;right:0;height:26px}
.top-band .stripe{position:absolute;left:0;right:0;top:8px;height:6px;background:var(--red)}
.tag-square{position:absolute;top:2px;width:26px;height:26px;background:var(--purple)}
h2{font-size:10.5px;font-weight:700;text-transform:uppercase;line-height:1.15;margin-bottom:6px;color:#111}
p{margin-bottom:5px;text-align:justify}
.photo{display:block;width:100%;margin:5px 0 7px}
.photo--park{height:120px;background:linear-gradient(180deg,#c9c4b0 0%,#a9b58a 45%,var(--grass) 100%)}
.quote{font-style:italic;margin:6px 0 8px;padding-bottom:8px;border-bottom:1px dashed var(--rule)}
.help-list{list-style:disc;padding-left:12px;margin-top:4px}
.help-list li{margin-bottom:3px}
.contact{text-align:center;margin-top:14px;font-size:7px;line-height:1.4}
.brand{font-weight:700;color:var(--purple);font-size:15px;line-height:1.05;text-align:center;margin-bottom:6px}
.brand--cover{font-size:22px;text-align:left}
.footer-band{position:absolute;left:0;right:0;bottom:0;height:22px;background:var(--red);color:#fff;font-size:7.6px;font-weight:700;display:flex;align-items:center;justify-content:center}
.cover-title{margin-top:14px;text-transform:uppercase;line-height:1.05}
.cover-title .l1{color:var(--purple);font-size:15px}
.cover-title .l2{color:var(--red);font-size:17px;font-weight:700}
.cover-title .l3{color:var(--purple);font-size:14px;text-transform:none;display:block}
.photo--cover{position:absolute;left:0;right:0;top:112px;height:290px;background:linear-gradient(180deg,#d9dfe0 0%,#7f9a6a 35%,#3d4f63 62%,#b59a62 100%)}
.cover-rule{position:absolute;left:0;right:0;top:402px;height:6px;background:var(--red)}
.cover-brand{position:absolute;left:24px;bottom:30px}
.photo-row{display:grid;gap:4px;margin:4px 0 8px}
.photo-row--two{grid-template-columns:1fr 1fr}
.ph{height:70px}
.ph--grass{background:linear-gradient(180deg,#b6c7a0,#5f8a3e)}
.ph--field{background:linear-gradient(180deg,#cfd7c2,#7ea35a)}
.ph--water{height:96px;background:linear-gradient(180deg,#9fc3dc,#4a86b5)}
.ph--group{height:110px;background:linear-gradient(180deg,#8fae6e,#9a5a6a)}
.ph--tall{height:88px}
.card{position:absolute;left:12px;right:12px;top:14px;bottom:34px;border:1px dashed var(--rule);padding:10px 12px}
.card-lead{font-weight:700;text-align:center;font-size:8px;margin-bottom:4px}
.card h3{font-size:9px;text-align:center;text-transform:uppercase;margin-bottom:8px}
.field{display:flex;gap:4px;margin-bottom:7px}
.field span.line{flex:1;border-bottom:1px solid #777}
.check{display:flex;gap:5px;margin-bottom:6px}
.box{flex:none;width:7px;height:7px;border:1px solid #555;margin-top:1px}
.small{font-size:6.2px}
</style>
</head>
<body>

<section class="sheet sheet--outside">
  <article class="panel panel--story">
    <div class="top-band"><div class="stripe"></div><div class="tag-square" style="right:14px"></div></div>
    <h2>The Story of Bright Harbor<br>Youth Camps</h2>
    <p>According to the Coastal Youth Welfare Study, 1 out of 3 girls and 1 out of 6 boys experience some form of abuse or neglect before age 18. Over three million reports are filed each year across the country, and these are only the cases that are known.</p>
    <div class="photo photo--park" role="img" aria-label="Photo of a volunteer walking hand in hand with a camper across a grassy field"></div>
    <p>Bright Harbor Youth Camps, Inc. (BHYC) was founded in 1985 as a ministry of the local church. Today the network includes 188 church-sponsored camps across the U.S. and 23 camps in four foreign countries, serving thousands of children every summer.</p>
    <p>The goal of BHYC is to show children that a positive life is possible. Through a week of fun, structure and caring adults, campers build memories that give them hope and a reason to feel good about themselves and their future.</p>
  </article>

  <article class="panel panel--involve">
    <div class="top-band"><div class="stripe"></div><div class="tag-square" style="left:14px"></div></div>
    <h2>How You Can Be Part<br>of the Bright Harbor Family</h2>
    <p>Children in foster care hurt. Not only do they often carry painful memories of abuse and abandonment, but they also carry worries about their future. One child from another BHY camp wrote this:</p>
    <p class="quote">I'm tired. Not work tired. Not school tired. Not sleep tired. Just tired.<br>I'm moving tired.<br>I'm tired of missing people.<br>I'm tired of foster care tired.</p>
    <p>BHYC seeks to provide positive, lasting memories of a loving Christian environment for these hurting children in our community. You can help show God's love to these children by supporting BHYC in a variety of ways, including:</p>
    <ul class="help-list">
      <li>Praying for the campers, counselors and staff</li>
      <li>Donating needed supplies for activities, crafts, dress-up, sports and birthday party</li>
      <li>Making a tax-deductible donation to support or fully sponsor a child</li>
      <li>Assisting with camper registration at church</li>
      <li>Helping at the Big Camp Birthday Bash</li>
      <li>Volunteering at the Homecoming Supper at church</li>
      <li>Serving one week at camp as a counselor or support staff</li>
    </ul>
    <div class="contact">
      <div class="brand">Bright Harbor<br>YOUTH</div>
      Harborview Community Church<br>1200 Lantern Hill Road, Seabrook, CA 90000<br>(555) 555-0142<br>bhyc@example-mail.net
    </div>
    <div class="footer-band">www.ventura.brightharboryouth-example.org</div>
  </article>

  <article class="panel panel--cover">
    <div class="cover-title">
      <span class="l1">Creating</span><br>
      <span class="l2">Positive Memories</span>
      <span class="l3">for Abused Kids</span>
    </div>
    <div class="photo--cover" role="img" aria-label="Photo of a boy seen from behind, sitting on a rock overlooking green hills"></div>
    <div class="cover-rule"></div>
    <div class="cover-brand"><div class="brand brand--cover">Bright Harbor<br>YOUTH</div></div>
  </article>
</section>

<section class="sheet sheet--inside">
  <article class="panel panel--reality">
    <div class="top-band"><div class="stripe"></div><div class="tag-square" style="right:14px"></div></div>
    <h2>A Startling Reality</h2>
    <div class="ph ph--grass ph--tall" role="img" aria-label="Photo of a camper and counselor exploring a grassy hillside"></div>
    <p style="margin-top:6px">It happens more often than any of us want to believe. Every year, over 3 million reports of child abuse are made across the country. Children are neglected, abandoned, emotionally harmed and mistreated by those who should protect them. Many of these children find themselves in foster care, feeling unloved and alone.</p>
    <div class="ph ph--water" role="img" aria-label="Photo of children splashing down a water slide at camp"></div>
    <p style="margin-top:6px">At Bright Harbor Youth Camps, campers experience a week of love, helping them realize that they are valuable to themselves, valuable to others, and valuable to God.</p>
    <div class="ph ph--group" role="img" aria-label="Photo of a group of girls hugging together on the lawn"></div>
  </article>

  <article class="panel panel--opportunity">
    <div class="photo-row photo-row--two" style="margin-top:-14px">
      <div class="ph ph--field" role="img" aria-label="Photo of campers playing a game in a park"></div>
      <div class="ph ph--grass" role="img" aria-label="Photo of kids and counselors relaxing under trees"></div>
    </div>
    <h2>A Wonderful Opportunity</h2>
    <p>Bright Harbor Youth Camp of Ventura is a residential camp for boys and girls, ages 7 to 11, who have been abused. Campers enjoy swimming, hiking, horseback riding, arts and crafts, a birthday party and campfires, all with trained, caring counselors who give each child focused attention.</p>
    <p>Activities include hiking, swimming, horseback riding, a petting zoo, crafts, games and a big birthday celebration for everyone, complete with cake and presents.</p>
    <div class="photo-row photo-row--two">
      <div class="ph ph--field" role="img" aria-label="Photo of campers running a relay race"></div>
      <div class="ph ph--grass" role="img" aria-label="Photo of kids playing on a sunny field"></div>
    </div>
    <p>For the first time, many of these youngsters will know what it feels like to have a caring "family" to shower them with encouragement and join in all kinds of fun games, activities and stories.</p>
    <p>This kind of love and security is so new for many of these children that a week at camp is often a life-changing experience, one that can sustain them all year long.</p>
  </article>

  <article class="panel panel--card">
    <div class="card">
      <div class="card-lead">When one counselor says "YES!" two campers start packing.</div>
      <h3>Interest Card</h3>
      <div class="check small"><span class="box"></span>I want to say "YES" and be a part of this Bright Harbor family.</div>
      <div class="field small">Name:<span class="line"></span></div>
      <div class="field small">Address:<span class="line"></span></div>
      <div class="field small">City/State/Zip:<span class="line"></span></div>
      <div class="field small">Phone:<span class="line"></span></div>
      <div class="field small">E-mail:<span class="line"></span></div>
      <div class="check small"><span class="box"></span>Please add me to the BHYC e-mail list and prayer team.</div>
      <div class="check small"><span class="box"></span>I'll commit to praying for BHYC campers, counselors and staff.</div>
      <div class="check small"><span class="box"></span>I'm interested in serving for a week at camp as a counselor or staff.</div>
      <div class="check small"><span class="box"></span>I'd like to donate $_______ (checks payable to Harborview Community Church, memo "BHYC").</div>
      <div class="field small"><span class="box"></span>Other:<span class="line"></span></div>
      <div class="contact" style="margin-top:10px">
        <div class="brand">Bright Harbor<br>YOUTH</div>
        Harborview Community Church<br>1200 Lantern Hill Road, Seabrook, CA 90000<br>(555) 555-0142<br>bhyc@example-mail.net
      </div>
    </div>
    <div class="footer-band">www.ventura.brightharboryouth-example.org</div>
  </article>
</section>

</body>
</html>
```